Redesign one screen in a mobile app

I have an app called Toasts and Tallies (available on iOS and Android). This app allows wedding guests to bet on things that happen during a wedding they are attending (think: will the groom cry when the bride walks down the aisle...). The event is set up by someone called the "event leader", typically this is the bride or the groom.

Once event details, bets, and $ values of the bets are entered, the event leader publishes the event and gets to the event detail homescreen, where they can manage their event. The three main things they can do are:

1.) Share the event with other guests to join in the betting.
2.) Edit the event -- add, change, or delete bets.
3.) Add a co-organizer. If you are the bride or the groom, you want someone else managing the event on your wedding day.

I'd like to redesign this page, make it simpler, and *focus attention on sharing the event.* The biggest goal of this page is getting event leaders to share the event. We want them to invite as many wedding guests as possible.

To that end, I would like to also introducing "sharing tiers" to entice more sharing and I'd like this to be something event leaders can easily see once they hit the event homescreen. Tiers are as follows:
Share with 1 guest, unlock co-organizer feature.
Share with 5 guests, unlock physical placard with custom QR code.
Share with 10 guests, we split our proceeds with the bride and groom.
Share with 20 guests, you are entered into $250 monthly raffle.

Some additional requests:
+ Please do not use current fonts. We want new fonts that are cleaner.
+ Share options should stay the same (copy, share, QR code)
+ Need to keep "help" question mark on page as well.
+ Maintain colors generally. Red button color must be kept as is because it's used throughout app. Slight variations to other colors OK.
+ Navigation at bottom must remain.
+ Feel free to add moving elements as well, like gifs.
+ Final design delivered in Figma.
Updates

Submissions need to be app designs. Not webpages.

The current actions shown on the page need to remain - share event, edit event, add a Co-Organizer. But the goal of the design is to make the page simpler, not more complicated.

Sharing tiers can be a separate screen, linked from the event home screen. This information does not need to live on the same page!

Target Market(s)

25-40 year olds

Industry/Entity Type

Mobile Apps - Betting

Font styles to use
Sans Serif
Other font styles liked:
• I like poppins, but open to other options.

Requirements
Must have
• Fun design that focuses on sharing an event. Design delievered in Figma.

```html
<!DOCTYPE html>
<html lang="en">
<head>
<meta charset="utf-8">
<title>Toasts and Tallies – Event Details options</title>
<link href="https://fonts.googleapis.com/css2?family=Poppins:wght@300;400;500;600;700&display=swap" rel="stylesheet">
<style>
  :root{
    --board:#707789;
    --screen:#f2f3f8;
    --card:#ffffff;
    --soft:#f1f2f7;
    --ink:#2e3038;
    --muted:#4a4c55;
    --red:#e06152;
    --purple:#8c1fa3;
    --bar:#353a42;
  }
  *{box-sizing:border-box;margin:0;padding:0}
  html,body{width:811px;height:1200px;overflow:hidden;background:#fff;font-family:'Poppins',sans-serif;color:var(--ink)}
  .frame-label{position:absolute;left:28px;top:3px;width:124px;height:21px;background:var(--board);border:1px solid #5b6172;border-radius:3px;color:#fff;font-size:6.6px;line-height:19px;padding-left:4px;white-space:nowrap;overflow:hidden;letter-spacing:-.1px}
  .board{position:absolute;left:28px;top:28px;width:755px;height:1145px;background:var(--board)}
  .board-title{position:absolute;left:72px;top:36px;color:#fff;font-size:30px;font-weight:700;letter-spacing:-.2px}
  .phone{position:absolute;top:109px;width:269px;background:var(--screen);overflow:hidden}
  .phone--one{left:72px;height:897px}
  .phone--two{left:401px;height:959px}
  .round-btn{position:absolute;top:35px;width:30px;height:30px;border-radius:50%;background:#fff;display:flex;align-items:center;justify-content:center}
  .screen-title{position:absolute;left:12px;top:82px;font-size:18px;font-weight:300;color:var(--ink)}
  .card{position:absolute;left:14px;width:241px;background:var(--card);border-radius:16px}
  .event-photo{position:absolute;left:12px;top:12px;width:76px;height:76px;border-radius:6px;background:linear-gradient(160deg,#8a7a62 0%,#5f5a45 40%,#2f3527 65%,#7b6b55 100%)}
  .event-name{position:absolute;left:94px;top:11px;width:146px;font-size:13.8px;line-height:16.5px;font-weight:700;color:#3a3c44;letter-spacing:-.1px}
  .meta{position:absolute;left:94px;display:flex;align-items:center;gap:5px;font-size:10.5px;font-weight:600;color:#3a3c44}
  .meta--small{font-size:8.5px;font-weight:400}
  .bets-pill{position:absolute;left:12px;top:113px;width:76px;height:39px;border-radius:10px;background:var(--soft);display:flex;align-items:center;justify-content:center;gap:4px;font-size:8.5px}
  .level-btn{position:absolute;left:94px;top:113px;width:135px;height:39px;border-radius:9px;background:linear-gradient(90deg,var(--red) 0%,#d64f68 55%,var(--purple) 100%);display:flex;align-items:center;color:#fff;font-size:8.5px;font-weight:600}
  .level-num{width:26px;height:26px;margin:0 18px 0 6px;border:2px solid #fff;border-radius:5px;display:flex;align-items:center;justify-content:center;font-size:13px;font-weight:700}
  .section-title{position:absolute;left:14px;font-size:11.5px;font-weight:600;color:#3a3c44}
  .body-copy{position:absolute;left:12px;width:222px;font-size:8.2px;line-height:12.4px;color:#3a3c44;letter-spacing:-.05px}
  .link-field{position:absolute;left:12px;top:70px;width:217px;height:25px;border-radius:8px;background:var(--soft);font-size:6.2px;line-height:25px;padding-left:8px;color:#4a4c55;white-space:nowrap;overflow:hidden}
  .share-row{position:absolute;left:12px;top:102px;display:flex;gap:3px}
  .red-btn{height:33px;border-radius:7px;background:var(--red);color:#fff;font-size:7.5px;font-weight:600;display:flex;align-items:center;justify-content:center;gap:4px}
  .share-row .red-btn{width:70px}
  .edit-btn{position:absolute;left:12px;top:44px;width:217px}
  .organizers{position:absolute;left:12px;top:94px;width:217px;border-radius:10px;background:var(--soft)}
  .organizers-head{position:absolute;left:11px;top:10px;font-size:9.5px;color:#3a3c44}
  .plus{position:absolute;left:190px;top:10px}
  .person{position:absolute;left:11px;width:195px;height:51px;border-radius:6px;background:#fff}
  .avatar{position:absolute;left:10px;top:8px;width:35px;height:35px;border-radius:50%}
  .avatar--a{background:radial-gradient(circle at 50% 45%,#b98b6c 0 35%,#3f4a38 70%)}
  .avatar--b{background:radial-gradient(circle at 50% 45%,#e4c2a6 0 35%,#6fa7b9 70%)}
  .person-name{position:absolute;left:57px;top:12px;font-size:8.6px;color:#3a3c44}
  .person-role{position:absolute;left:57px;top:26px;font-size:7px;color:#4a4c55}
  .tabbar{position:absolute;left:0;width:269px;height:55px;background:#fff;border-radius:22px 22px 0 0}
  .tab-home{position:absolute;left:40px;top:7px;width:36px;height:36px;border-radius:50%;background:var(--red);display:flex;align-items:center;justify-content:center}
  .tab{position:absolute;top:9px;width:36px;height:32px;border-radius:7px;background:var(--soft);display:flex;flex-direction:column;align-items:center;justify-content:center;gap:1px;font-size:5px;color:#3a3c44}
  .homebar{position:absolute;left:0;width:269px;height:14px;background:var(--bar)}
  .homebar::after{content:"";position:absolute;left:86px;top:5px;width:96px;height:3px;border-radius:2px;background:#fff}
</style>
</head>
<body>
<div class="frame-label">Options for different fields filling</div>
<main class="board">
  <h1 class="board-title">Options for different fields filling</h1>

  <!-- Screen variant: long title, single organizer -->
  <section class="phone phone--one">
    <div class="round-btn" style="left:13px"><svg width="14" height="14" viewBox="0 0 14 14"><path d="M12 7H2M6 3L2 7l4 4" fill="none" stroke="#2e3038" stroke-width="1.3" stroke-linecap="round" stroke-linejoin="round"/></svg></div>
    <div class="round-btn" style="left:225px;font-size:19px;font-weight:400">?</div>
    <h2 class="screen-title">Event Details</h2>

    <div class="card" style="top:113px;height:162px">
      <div class="event-photo" role="img" aria-label="Photo of a dark green off-road vehicle on a dirt mountain road"></div>
      <div class="event-name">Trail Drive or Other Name</div>
      <div class="meta" style="top:49px"><svg width="13" height="13" viewBox="0 0 14 14"><circle cx="7" cy="7" r="6" fill="none" stroke="#3a3c44" stroke-width="1.2"/><circle cx="7" cy="7" r="2.4" fill="none" stroke="#3a3c44" stroke-width="1.2"/></svg>Missouri</div>
      <div class="meta meta--small" style="top:75px"><svg width="13" height="13" viewBox="0 0 14 14"><rect x="1.5" y="2.5" width="11" height="10" rx="2" fill="none" stroke="#3a3c44" stroke-width="1.1"/><path d="M4 1v3M10 1v3M4 7h6M4 9.5h4" stroke="#3a3c44" stroke-width="1.1"/></svg>Mar 03<span style="width:14px"></span><svg width="13" height="13" viewBox="0 0 14 14"><circle cx="7" cy="7" r="6" fill="none" stroke="#3a3c44" stroke-width="1.2"/><path d="M7 3.5V7l2 2" fill="none" stroke="#3a3c44" stroke-width="1.2"/></svg>05:00 PM</div>
      <div class="bets-pill"><svg width="14" height="14" viewBox="0 0 14 14"><path d="M3 3l7-1 1 3-3 8-5-2z" fill="none" stroke="#3a3c44" stroke-width="1.2" stroke-linejoin="round"/></svg>1000 Bets</div>
      <div class="level-btn"><span class="level-num">1</span>Go To Next Level</div>
    </div>

    <h3 class="section-title" style="top:285px">Share Your Event</h3>
    <div class="card" style="top:307px;height:146px">
      <p class="body-copy" style="top:11px">Invite guests to join by sharing the event below. Each guest pays $2.99 to join, and if 10+ guests join in the fun, we share the proceeds with the bride and groom!</p>
      <div class="link-field">https://links.toastsandtallies.com/8saCZe8lMhX6bsJWA</div>
      <div class="share-row">
        <div class="red-btn"><svg width="12" height="12" viewBox="0 0 12 12"><path d="M5 7l2-2M4.5 5.5L3 7a1.8 1.8 0 002.5 2.5L7 8M7.5 6.5L9 5a1.8 1.8 0 00-2.5-2.5L5 4" fill="none" stroke="#fff" stroke-width="1.1" stroke-linecap="round"/></svg>Copy</div>
        <div class="red-btn"><svg width="12" height="12" viewBox="0 0 12 12"><circle cx="3" cy="6" r="1.6" fill="none" stroke="#fff"/><circle cx="9" cy="2.8" r="1.6" fill="none" stroke="#fff"/><circle cx="9" cy="9.2" r="1.6" fill="none" stroke="#fff"/><path d="M4.4 5.2l3.2-1.6M4.4 6.8l3.2 1.6" stroke="#fff"/></svg>Share</div>
        <div class="red-btn"><svg width="12" height="12" viewBox="0 0 12 12"><rect x="1" y="1" width="4" height="4" fill="none" stroke="#fff"/><rect x="7" y="1" width="4" height="4" fill="none" stroke="#fff"/><rect x="1" y="7" width="4" height="4" fill="none" stroke="#fff"/><path d="M7 7h1.5v1.5H7zM9.5 9.5H11V11H9.5zM9.5 7H11v1M7 10v1h1" fill="#fff" stroke="#fff" stroke-width=".5"/></svg>QR Code</div>
      </div>
    </div>

    <h3 class="section-title" style="top:461px">Edit Your Event</h3>
    <div class="card" style="top:483px;height:87px">
      <p class="body-copy" style="top:11px">Change event details, add or delete bets, and change answer choices below.</p>
      <div class="red-btn edit-btn"><svg width="13" height="13" viewBox="0 0 14 14"><path d="M2 12l1-3.5L10 1.5l2.5 2.5-7 7z" fill="#fff"/></svg>Edit Your Event</div>
    </div>

    <h3 class="section-title" style="top:578px">Assign a Co-Organizer</h3>
    <div class="card" style="top:600px;height:205px">
      <p class="body-copy" style="top:11px">If a bride or groom created this event, you’ll want to assign a guest to be the co-organizer. This allows them to manage the event going forward, closing out all bets as they happen during the wedding weekend. Your co-organizer will get a notification to take over!</p>
      <div class="organizers" style="height:101px">
        <div class="organizers-head">Event Organizers</div>
        <svg class="plus" width="16" height="16" viewBox="0 0 16 16"><circle cx="8" cy="8" r="7" fill="none" stroke="#3a3c44" stroke-width="1.1"/><path d="M8 4.5v7M4.5 8h7" stroke="#3a3c44" stroke-width="1.1"/></svg>
        <div class="person" style="top:39px">
          <div class="avatar avatar--a" role="img" aria-label="Profile photo of the organizer"></div>
          <div class="person-name">Dan Morrow</div>
          <div class="person-role">Organazer</div>
        </div>
      </div>
    </div>

    <nav class="tabbar" style="top:828px">
      <div class="tab-home"><svg width="16" height="16" viewBox="0 0 16 16"><path d="M3 7l5-4 5 4v6H3z" fill="none" stroke="#fff" stroke-width="1.4" stroke-linejoin="round"/></svg></div>
      <div class="tab" style="left:116px"><svg width="14" height="14" viewBox="0 0 14 14"><path d="M3 3l7-1 1 3-3 8-5-2z" fill="none" stroke="#3a3c44" stroke-width="1.2" stroke-linejoin="round"/></svg>My Bets</div>
      <div class="tab" style="left:192px"><svg width="14" height="14" viewBox="0 0 14 14"><path d="M5 13V6h4v7M1.5 13V9H5M9 10h3.5v3M1 13h12" fill="none" stroke="#3a3c44" stroke-width="1.1"/><path d="M7 1l.7 1.4 1.5.2-1.1 1 .3 1.5L7 4.4l-1.4.7.3-1.5-1.1-1 1.5-.2z" fill="none" stroke="#3a3c44" stroke-width=".8"/></svg>Leaders</div>
    </nav>
    <div class="homebar" style="top:883px"></div>
  </section>

  <!-- Screen variant: short title, two organizers -->
  <section class="phone phone--two">
    <div class="round-btn" style="left:13px"><svg width="14" height="14" viewBox="0 0 14 14"><path d="M12 7H2M6 3L2 7l4 4" fill="none" stroke="#2e3038" stroke-width="1.3" stroke-linecap="round" stroke-linejoin="round"/></svg></div>
    <div class="round-btn" style="left:225px;font-size:19px;font-weight:400">?</div>
    <h2 class="screen-title">Event Details</h2>

    <div class="card" style="top:113px;height:162px">
      <div class="event-photo" role="img" aria-label="Photo of a dark green off-road vehicle on a dirt mountain road"></div>
      <div class="event-name">Trail Drive</div>
      <div class="meta" style="top:32px"><svg width="13" height="13" viewBox="0 0 14 14"><circle cx="7" cy="7" r="6" fill="none" stroke="#3a3c44" stroke-width="1.2"/><circle cx="7" cy="7" r="2.4" fill="none" stroke="#3a3c44" stroke-width="1.2"/></svg>Missouri</div>
      <div class="meta meta--small" style="top:58px"><svg width="13" height="13" viewBox="0 0 14 14"><rect x="1.5" y="2.5" width="11" height="10" rx="2" fill="none" stroke="#3a3c44" stroke-width="1.1"/><path d="M4 1v3M10 1v3M4 7h6M4 9.5h4" stroke="#3a3c44" stroke-width="1.1"/></svg>Mar 03<span style="width:14px"></span><svg width="13" height="13" viewBox="0 0 14 14"><circle cx="7" cy="7" r="6" fill="none" stroke="#3a3c44" stroke-width="1.2"/><path d="M7 3.5V7l2 2" fill="none" stroke="#3a3c44" stroke-width="1.2"/></svg>05:00 PM</div>
      <div class="bets-pill"><svg width="14" height="14" viewBox="0 0 14 14"><path d="M3 3l7-1 1 3-3 8-5-2z" fill="none" stroke="#3a3c44" stroke-width="1.2" stroke-linejoin="round"/></svg>17 Bets</div>
      <div class="level-btn"><span class="level-num">3</span>Go To Next Level</div>
    </div>

    <h3 class="section-title" style="top:285px">Share Your Event</h3>
    <div class="card" style="top:307px;height:146px">
      <p class="body-copy" style="top:11px">Invite guests to join by sharing the event below. Each guest pays $2.99 to join, and if 10+ guests join in the fun, we share the proceeds with the bride and groom!</p>
      <div class="link-field">https://links.toastsandtallies.com/8saCZe8lMhX6bsJWA</div>
      <div class="share-row">
        <div class="red-btn"><svg width="12" height="12" viewBox="0 0 12 12"><path d="M5 7l2-2M4.5 5.5L3 7a1.8 1.8 0 002.5 2.5L7 8M7.5 6.5L9 5a1.8 1.8 0 00-2.5-2.5L5 4" fill="none" stroke="#fff" stroke-width="1.1" stroke-linecap="round"/></svg>Copy</div>
        <div class="red-btn"><svg width="12" height="12" viewBox="0 0 12 12"><circle cx="3" cy="6" r="1.6" fill="none" stroke="#fff"/><circle cx="9" cy="2.8" r="1.6" fill="none" stroke="#fff"/><circle cx="9" cy="9.2" r="1.6" fill="none" stroke="#fff"/><path d="M4.4 5.2l3.2-1.6M4.4 6.8l3.2 1.6" stroke="#fff"/></svg>Share</div>
        <div class="red-btn"><svg width="12" height="12" viewBox="0 0 12 12"><rect x="1" y="1" width="4" height="4" fill="none" stroke="#fff"/><rect x="7" y="1" width="4" height="4" fill="none" stroke="#fff"/><rect x="1" y="7" width="4" height="4" fill="none" stroke="#fff"/><path d="M7 7h1.5v1.5H7zM9.5 9.5H11V11H9.5zM9.5 7H11v1M7 10v1h1" fill="#fff" stroke="#fff" stroke-width=".5"/></svg>QR Code</div>
      </div>
    </div>

    <h3 class="section-title" style="top:461px">Edit Your Event</h3>
    <div class="card" style="top:483px;height:87px">
      <p class="body-copy" style="top:11px">Change event details, add or delete bets, and change answer choices below.</p>
      <div class="red-btn edit-btn"><svg width="13" height="13" viewBox="0 0 14 14"><path d="M2 12l1-3.5L10 1.5l2.5 2.5-7 7z" fill="#fff"/></svg>Edit Your Event</div>
    </div>

    <h3 class="section-title" style="top:578px">Assign a Co-Organizer</h3>
    <div class="card" style="top:600px;height:267px">
      <p class="body-copy" style="top:11px">If a bride or groom created this event, you’ll want to assign a guest to be the co-organizer. This allows them to manage the event going forward, closing out all bets as they happen during the wedding weekend. Your co-organizer will get a notification to take over!</p>
      <div class="organizers" style="height:163px">
        <div class="organizers-head">Event Organizers</div>
        <svg class="plus" width="16" height="16" viewBox="0 0 16 16"><circle cx="8" cy="8" r="7" fill="none" stroke="#3a3c44" stroke-width="1.1"/><path d="M8 4.5v7M4.5 8h7" stroke="#3a3c44" stroke-width="1.1"/></svg>
        <div class="person" style="top:39px">
          <div class="avatar avatar--a" role="img" aria-label="Profile photo of the organizer"></div>
          <div class="person-name">Dan Morrow</div>
          <div class="person-role">Organizer</div>
        </div>
        <div class="person" style="top:101px">
          <div class="avatar avatar--b" role="img" aria-label="Profile photo of the co-organizer"></div>
          <div class="person-name">Lena Morrow</div>
          <div class="person-role">Co-organizer</div>
        </div>
      </div>
    </div>

    <nav class="tabbar" style="top:890px">
      <div class="tab-home"><svg width="16" height="16" viewBox="0 0 16 16"><path d="M3 7l5-4 5 4v6H3z" fill="none" stroke="#fff" stroke-width="1.4" stroke-linejoin="round"/></svg></div>
      <div class="tab" style="left:116px"><svg width="14" height="14" viewBox="0 0 14 14"><path d="M3 3l7-1 1 3-3 8-5-2z" fill="none" stroke="#3a3c44" stroke-width="1.2" stroke-linejoin="round"/></svg>My Bets</div>
      <div class="tab" style="left:192px"><svg width="14" height="14" viewBox="0 0 14 14"><path d="M5 13V6h4v7M1.5 13V9H5M9 10h3.5v3M1 13h12" fill="none" stroke="#3a3c44" stroke-width="1.1"/><path d="M7 1l.7 1.4 1.5.2-1.1 1 .3 1.5L7 4.4l-1.4.7.3-1.5-1.1-1 1.5-.2z" fill="none" stroke="#3a3c44" stroke-width=".8"/></svg>Leaders</div>
    </nav>
    <div class="homebar" style="top:945px"></div>
  </section>
</main>
</body>
</html>
```